Stationary & Business cards for Onsite Wastewater Company
Brindlecove Septic Systems Ltd.
Stationary & Business cards for Onsite Wastewater Company - Construction
Creative Brief
Professional
Dwight Amberole
6172 Pellworth St. Langley, B.C. V3K8R2
dwight@brindlecoveseptic-example.com
brindlecoveseptic-example.com
I would like it to say: Design & Build on the front of the card
Open to ideas: maybe use the logo with black background
lanternmoth lanternmoth

```html
<!DOCTYPE html>
<html lang="en">
<head>
<meta charset="utf-8">
<title>Brindlecove Septic Systems Ltd. – Stationery Set</title>
<link href="https://fonts.googleapis.com/css2?family=Roboto:wght@400;700;900&display=swap" rel="stylesheet">
<style>
  :root{
    --backdrop:#707070;
    --paper:#ffffff;
    --ink:#1a1a1a;
    --muted:#7a7a7a;
    --blue:#1f86cf;
    --blue-light:#7cc3ee;
    --navy:#0c2f52;
    --black:#111111;
  }
  *{box-sizing:border-box;margin:0;padding:0}
  html,body{width:1200px;height:228px;overflow:hidden}
  body{background:var(--backdrop);font-family:"Roboto",Arial,sans-serif;color:var(--ink);position:relative}
  .item{position:absolute;background:var(--paper);overflow:hidden;box-shadow:1px 2px 4px rgba(0,0,0,.45)}
  .item.dark{background:var(--black)}
  .wave{position:absolute;left:0;width:100%}
  .wave.bottom{bottom:0}
  .wave.top{top:0;transform:scaleY(-1)}
  .brand{position:absolute;font-weight:900;color:var(--navy);letter-spacing:.2px;line-height:1;text-transform:uppercase;white-space:nowrap}
  .dark .brand{color:var(--paper)}
  .tagline{position:absolute;font-size:3.5px;color:var(--muted);text-transform:uppercase;letter-spacing:.3px;white-space:nowrap}
  .dark .tagline{color:var(--blue-light)}
  .fine{position:absolute;font-size:3px;line-height:1.4;color:var(--muted);white-space:nowrap}
  .dark .fine{color:#cfcfcf}
  .fax-title{position:absolute;font-weight:700;font-size:12px;color:var(--ink);line-height:1}
  .fax-table{position:absolute;border-collapse:collapse;font-size:3.2px;color:var(--muted)}
  .fax-table td{border-bottom:.5px solid #bbb;padding:1px 2px;width:32px}
  .disc{position:absolute;border-radius:50%;overflow:hidden;background:var(--paper);box-shadow:1px 2px 4px rgba(0,0,0,.45)}
  .disc .hole{position:absolute;left:50%;top:50%;width:14px;height:14px;margin:-7px 0 0 -7px;border-radius:50%;background:var(--backdrop);border:3px solid #d9d9d9}
</style>
</head>
<body>

<svg width="0" height="0" style="position:absolute" aria-hidden="true">
  <defs>
    <linearGradient id="band" x1="0" x2="1" y1="0" y2="0">
      <stop offset="0" stop-color="#0b4f8a"/>
      <stop offset=".55" stop-color="#1f86cf"/>
      <stop offset="1" stop-color="#8fd0f4"/>
    </linearGradient>
    <symbol id="swoosh" viewBox="0 0 100 30" preserveAspectRatio="none">
      <path d="M0 12 C30 2 60 26 100 8 L100 30 L0 30Z" fill="url(#band)"/>
      <path d="M0 18 C35 8 62 30 100 14 L100 30 L0 30Z" fill="#0c2f52"/>
      <path d="M0 12 C30 2 60 26 100 8" fill="none" stroke="#ffffff" stroke-width=".8"/>
    </symbol>
  </defs>
</svg>

<!-- Business cards -->
<div class="item card" style="left:6px;top:40px;width:60px;height:34px">
  <span class="brand" style="left:5px;top:10px;font-size:7px">Brindlecove</span>
  <span class="tagline" style="left:5px;top:19px">Design &amp; Build</span>
  <svg class="wave bottom" style="height:10px"><use href="#swoosh"/></svg>
</div>
<div class="item card" style="left:62px;top:48px;width:60px;height:34px">
  <span class="fine" style="left:3px;top:4px">Dwight Amberole<br>6172 Pellworth St. Langley, B.C.<br>V3K8R2<br>dwight@brindlecoveseptic-example.com</span>
  <svg class="wave bottom" style="height:8px"><use href="#swoosh"/></svg>
</div>
<div class="item card dark" style="left:6px;top:146px;width:60px;height:34px">
  <span class="brand" style="left:5px;top:10px;font-size:7px">Brindlecove</span>
  <span class="tagline" style="left:5px;top:19px">Design &amp; Build</span>
  <svg class="wave bottom" style="height:8px"><use href="#swoosh"/></svg>
</div>
<div class="item card" style="left:62px;top:154px;width:60px;height:34px">
  <span class="fine" style="left:3px;top:4px">Dwight Amberole<br>brindlecoveseptic-example.com</span>
  <svg class="wave bottom" style="height:8px"><use href="#swoosh"/></svg>
</div>

<!-- Letterheads -->
<div class="item letterhead" style="left:134px;top:24px;width:130px;height:178px">
  <span class="brand" style="right:8px;top:12px;font-size:9px">Brindlecove</span>
  <span class="tagline" style="right:8px;top:23px">Septic Systems Ltd.</span>
  <svg class="wave bottom" style="height:24px"><use href="#swoosh"/></svg>
</div>
<div class="item letterhead" style="left:270px;top:24px;width:130px;height:178px">
  <span class="brand" style="left:8px;top:12px;font-size:9px">Brindlecove</span>
  <span class="tagline" style="left:8px;top:23px">Septic Systems Ltd.</span>
  <span class="fine" style="left:8px;bottom:28px">6172 Pellworth St. Langley, B.C. V3K8R2</span>
  <svg class="wave bottom" style="height:22px"><use href="#swoosh"/></svg>
</div>

<!-- Fax sheet -->
<div class="item fax" style="left:406px;top:24px;width:130px;height:178px">
  <span class="brand" style="left:8px;top:10px;font-size:7px">Brindlecove</span>
  <span class="fax-title" style="left:8px;top:32px">Fax</span>
  <table class="fax-table" style="left:40px;top:32px">
    <tr><td>To:</td><td>From:</td></tr>
    <tr><td>Fax:</td><td>Pages:</td></tr>
    <tr><td>Phone:</td><td>Date:</td></tr>
  </table>
  <svg class="wave bottom" style="height:22px"><use href="#swoosh"/></svg>
</div>

<!-- Compliment slip -->
<div class="item slip" style="left:552px;top:104px;width:64px;height:34px">
  <span class="brand" style="left:5px;top:6px;font-size:5.5px">Brindlecove</span>
  <svg class="wave bottom" style="height:8px"><use href="#swoosh"/></svg>
</div>

<!-- DL envelope front -->
<div class="item envelope" style="left:552px;top:146px;width:108px;height:42px">
  <span class="brand" style="left:6px;top:6px;font-size:6px">Brindlecove</span>
  <svg class="wave bottom" style="height:10px"><use href="#swoosh"/></svg>
</div>

<!-- Envelope stack -->
<div class="item envelope dark" style="left:672px;top:104px;width:150px;height:44px">
  <svg class="wave top" style="height:14px"><use href="#swoosh"/></svg>
</div>
<div class="item envelope" style="left:678px;top:124px;width:150px;height:44px">
  <svg class="wave bottom" style="height:12px"><use href="#swoosh"/></svg>
</div>
<div class="item envelope" style="left:684px;top:144px;width:150px;height:44px">
  <span class="brand" style="left:7px;top:7px;font-size:6.5px">Brindlecove</span>
  <svg class="wave bottom" style="height:11px"><use href="#swoosh"/></svg>
</div>

<!-- Presentation folder -->
<div class="item folder" style="left:842px;top:6px;width:128px;height:214px">
  <span class="brand" style="left:10px;top:52px;font-size:10px">Brindlecove</span>
  <span class="tagline" style="left:10px;top:65px;font-size:4px">Septic Systems Ltd.</span>
  <svg class="wave top" style="height:30px"><use href="#swoosh"/></svg>
  <svg class="wave bottom" style="height:44px"><use href="#swoosh"/></svg>
</div>
<div class="item folder" style="left:972px;top:6px;width:128px;height:214px">
  <svg class="wave bottom" style="height:70px"><use href="#swoosh"/></svg>
  <div class="item card" style="left:48px;top:118px;width:32px;height:18px">
    <span class="brand" style="left:3px;top:7px;font-size:4px">Brindlecove</span>
  </div>
</div>

<!-- Disc -->
<div class="disc" style="left:1108px;top:12px;width:72px;height:72px">
  <span class="brand" style="left:14px;top:17px;font-size:6px">Brindlecove</span>
  <svg class="wave bottom" style="height:28px"><use href="#swoosh"/></svg>
  <div class="hole"></div>
</div>

</body>
</html>
```